Business Card for Jewelry Business

We need a new namecard design for a jewelry company based in Bangkok, Thailand. We have a new website recently and want the new namecard to reflect our new modern image. I have uploaded our old namecard to show you the information that needs to be on the namecard. Pls check our website www.qelburn.com for the new color scheme to help design the new namecard.

```html
<!DOCTYPE html>
<html lang="en">
<head>
<meta charset="utf-8">
<title>Qelburn Manufacturers – Business Card</title>
<link rel="stylesheet" href="https://fonts.googleapis.com/css2?family=Poppins:wght@400;500;700&display=swap">
<style>
  :root {
    --bg: #e9e9eb;
    --card: #ffffff;
    --teal: #4fc1c6;
    --navy: #14163a;
    --ink: #2b2b2f;
    --beige: #e4ddd2;
    --photo-dark: #2c2e31;
    --photo-mid: #6b6d70;
  }
  * { box-sizing: border-box; margin: 0; padding: 0; }
  html, body { width: 1200px; height: 800px; overflow: hidden; }
  body {
    background: var(--bg);
    font-family: "Poppins", sans-serif;
    position: relative;
  }
  .card {
    position: absolute;
    top: 245px;
    width: 540px;
    height: 310px;
    background: var(--card);
    border-radius: 22px;
    overflow: hidden;
    box-shadow: 0 10px 30px rgba(0,0,0,0.12);
  }
  .card--front { left: 50px; }
  .card--back { left: 610px; }

  /* Front */
  .brand {
    position: absolute;
    left: 0; right: 0; top: 105px;
    display: flex; align-items: center; justify-content: center; gap: 14px;
  }
  .brand__dot {
    width: 30px; height: 30px; border-radius: 50%;
    background: var(--teal);
  }
  .brand__name {
    font-weight: 500;
    font-size: 22px;
    letter-spacing: 3px;
    color: var(--navy);
    text-transform: uppercase;
  }
  .website {
    position: absolute;
    left: 0; right: 0; top: 205px;
    text-align: center;
    font-size: 15px;
    letter-spacing: 7px;
    color: var(--ink);
  }
  .website__domain { color: var(--teal); }

  /* Back */
  .back-art { position: absolute; inset: 0; }
  .emblem {
    position: absolute;
    left: 190px; top: 118px;
    width: 124px; height: 124px;
    border-radius: 50%;
    background: var(--card);
    border: 2px solid var(--beige);
    display: flex; align-items: center; justify-content: center;
  }
  .emblem__name {
    font-size: 12px; font-weight: 500; letter-spacing: 2px;
    color: var(--teal); text-transform: uppercase;
  }
  .details {
    position: absolute;
    right: 22px; top: 26px;
    text-align: right;
  }
  .details__name {
    font-weight: 700; font-size: 20px; color: var(--navy);
    letter-spacing: 0.3px; line-height: 1.1;
  }
  .details__title {
    font-size: 11.5px; color: var(--teal); margin-top: 3px;
  }
  .details__address {
    font-size: 9.6px; color: var(--ink); line-height: 1.45; margin-top: 12px;
  }
  .contacts { list-style: none; margin-top: 12px; }
  .contacts li {
    display: flex; align-items: center; justify-content: flex-end; gap: 6px;
    font-size: 9.6px; color: var(--ink); line-height: 1.5;
  }
  .contacts__icon {
    width: 12px; height: 12px; flex: none;
  }
</style>
</head>
<body>

<section class="card card--front" aria-label="Card front">
  <div class="brand">
    <span class="brand__dot"></span>
    <span class="brand__name">Qelburn Manufacturers</span>
  </div>
  <p class="website">www.<span class="website__domain">qelburn</span>.com</p>
</section>

<section class="card card--back" aria-label="Card back">
  <svg class="back-art" width="540" height="310" viewBox="0 0 540 310">
    <defs>
      <linearGradient id="photoTone" x1="0" y1="0" x2="1" y2="1">
        <stop offset="0" stop-color="#7b7d80"/>
        <stop offset="0.5" stop-color="#3a3c40"/>
        <stop offset="1" stop-color="#5a5550"/>
      </linearGradient>
    </defs>
    <path role="img" aria-label="Photo of a hand holding a silver flower pendant against a polishing wheel"
          d="M0,60 C110,20 220,20 250,120 C275,200 250,270 235,310 L0,310 Z" fill="url(#photoTone)"/>
    <path d="M0,60 C110,20 220,20 250,120 C275,200 250,270 235,310" fill="none" stroke="var(--teal)" stroke-width="4"/>
  </svg>

  <div class="emblem"><span class="emblem__name">Qelburn</span></div>

  <div class="details">
    <p class="details__name">NARA PETCHSAI</p>
    <p class="details__title">Sales &amp; Product Development Manager</p>
    <p class="details__address">128 Moo 7, Export Processing Zone 2<br>Bang Phli Industrial Estate<br>Bangkok, 10540 Thailand</p>
    <ul class="contacts">
      <li>+662 - 418-2293 - 5
        <svg class="contacts__icon" viewBox="0 0 12 12"><circle cx="6" cy="6" r="6" fill="var(--teal)"/><path d="M4 3.2 L5 4.6 L4.4 5.3 Q5 6.8 6.7 7.6 L7.4 7 L8.8 8 L8.2 8.9 Q5.5 8.8 3.3 4 Z" fill="#fff"/></svg>
      </li>
      <li>+662 - 551 - 3082
        <svg class="contacts__icon" viewBox="0 0 12 12"><circle cx="6" cy="6" r="6" fill="var(--teal)"/><rect x="3.2" y="4" width="5.6" height="4.2" rx="0.5" fill="#fff"/><rect x="4.2" y="2.8" width="3.6" height="1.6" fill="#fff"/></svg>
      </li>
      <li>nara@qelburn.com
        <svg class="contacts__icon" viewBox="0 0 12 12"><circle cx="6" cy="6" r="6" fill="var(--teal)"/><rect x="3" y="4" width="6" height="4.2" fill="#fff"/><path d="M3 4 L6 6.4 L9 4" fill="none" stroke="var(--teal)" stroke-width="0.7"/></svg>
      </li>
      <li>hello@qelburn.com
        <svg class="contacts__icon" viewBox="0 0 12 12"><circle cx="6" cy="6" r="6" fill="var(--teal)"/><rect x="3" y="4" width="6" height="4.2" fill="#fff"/><path d="M3 4 L6 6.4 L9 4" fill="none" stroke="var(--teal)" stroke-width="0.7"/></svg>
      </li>
      <li>Qelburn Manufacturers
        <svg class="contacts__icon" viewBox="0 0 12 12"><circle cx="6" cy="6" r="6" fill="var(--teal)"/></svg>
      </li>
      <li>@QelburnMfr
        <svg class="contacts__icon" viewBox="0 0 12 12"><circle cx="6" cy="6" r="6" fill="var(--teal)"/></svg>
      </li>
    </ul>
  </div>
</section>

</body>
</html>
```